Health & Fitness Author & Public Speaker Needs Visually Stunning Web Redesign!

It's time for a redesign of the home page for Verity Halloway's "Bright Fork Kitchen" website (www.brightforkkitchen-example.com). We have a VERY clear idea of what we want, so it really won't take a talented designer long to bring it to life.
The website itself is used to promote & sell her range of health & nutrition programs to a female audience, primarily aged 24 - 35 working in professional or semi professional occupations.
For a VERY comprehensive outline of exactly what we are after, please see the following attached files:
(1) 'Website - WireFrame' (layout, content/copy, visual design style we want along with the desired color scheme)
(2) 'Website - Style Guide' (these are the colours, and overall feel we want)
PLEASE REVIEW THIS IN FULL - THEY WILL GIVE YOU A VERY CLEAR IDEA OF WHAT WE WANT.
Most of the files you need are attached, but for more photos that you can use (of Verity, her programs, and food/meals) can be found at these URL's:
VERITY (profile photos):
https://www.filebinbox.example/sh/qm3rt8wpz1xkd7a/RtPlm4vaNe
ECOVERS
- Bright Fork Kitchen Guide (ebook): https://www.filebinbox.example/sh/wxtnvo5d274ku22/hBqYrsnoz3
- 21 Week Total Momentum Course (ecourse): https://www.filebinbox.example/sh/zopqinr6a2mhwyl/c-dg341oTR
- E-Magazine Issues:
https://www.filebinbox.example/sh/4pzmkar2s9vtyw/57LeWcdDxpB
STOCK IMAGES:
https://www.filebinbox.example/sh/k2qowr8atbnzlx/Qe3HT5mmDy
As we will need to revamp our existing Facebook page & other printed material, there may be the potential for further work for the successful designer in the future.
Thanks & Good Luck!
Declan Furrow
Marketing & Business Development Manager
Bright Fork Kitchen

```html
<!DOCTYPE html>
<html lang="en">
<head>
<meta charset="utf-8">
<title>Bright Fork Kitchen — You Don't Need Another Diet</title>
<link href="https://fonts.googleapis.com/css2?family=Open+Sans:wght@400;600;700;800&family=Kalam:wght@700&display=swap" rel="stylesheet">
<style>
:root{
  --pink:#e8407a;
  --pink-soft:#fbe3ec;
  --green:#8dc63f;
  --ink:#4a4a4a;
  --muted:#6f6f6f;
  --line:#e4e4e4;
  --panel:#f2f2f2;
  --white:#fff;
}
*{box-sizing:border-box;margin:0;padding:0}
html,body{width:1200px;height:2684px;overflow:hidden}
body{font-family:"Open Sans",Arial,sans-serif;color:var(--ink);background:var(--white);display:flex;flex-direction:column}
.site-header{height:100px;flex:none;display:flex;align-items:center;justify-content:space-between;padding:0 48px}
.brand{display:flex;align-items:center;gap:12px;font-weight:700;font-size:28px;color:var(--pink)}
.brand-dot{width:24px;height:24px;border-radius:50%;background:var(--green)}
.main-nav{display:flex;gap:28px;align-items:center;font-size:14px;font-weight:700;color:var(--green);letter-spacing:.3px}
.main-nav .shop{background:var(--pink);color:var(--white);padding:9px 18px}
.hero{height:640px;flex:none;background:linear-gradient(135deg,#6f9a4a 0%,#a9c27a 35%,#c9b08e 60%,#5f7f3c 100%);display:flex;align-items:center;justify-content:center}
.hero h1{color:var(--white);font-weight:800;font-size:54px;line-height:1.15;text-align:center;text-transform:uppercase;text-shadow:0 2px 6px rgba(0,0,0,.35);margin-top:140px}
.optin-bar{height:120px;flex:none;background:var(--pink);display:flex;align-items:center;justify-content:space-between;padding:0 48px;color:var(--white)}
.optin-copy strong{display:block;font-size:24px;font-weight:700;margin-bottom:4px}
.optin-copy span{font-size:14px;display:block;max-width:480px;line-height:1.4}
.optin-form{display:flex;gap:10px}
.field{width:180px;height:44px;background:var(--white);color:#999;font-size:12px;padding:0 12px;display:flex;align-items:center;text-transform:uppercase}
.btn-yes{height:44px;padding:0 20px;background:var(--white);color:var(--green);border:2px solid var(--green);font-weight:800;font-size:16px;display:flex;align-items:center}
.content{flex:1;min-height:0;display:flex;gap:36px;padding:36px 48px 20px;overflow:hidden}
.article{width:712px;font-size:15px;line-height:1.6;color:var(--muted)}
.article h2{color:var(--pink);font-size:23px;font-weight:600;line-height:1.3;margin-bottom:14px}
.article h3{color:var(--pink);font-size:19px;font-weight:600;margin:20px 0 8px}
.article p{margin-bottom:12px}
.article ul{margin:0 0 14px 22px}
.article li{margin-bottom:2px}
.article .lead{color:var(--pink);font-weight:700}
.sidebar{width:356px}
.endorsed{border:1px solid var(--line);padding:22px;text-align:center}
.endorsed h4{font-size:11px;color:var(--muted);letter-spacing:1px;margin-bottom:18px}
.press{font-weight:600;color:var(--ink);font-size:22px;margin:16px 0;display:flex;align-items:center;justify-content:center;gap:10px}
.promo-photo{height:300px;margin-top:24px;background:linear-gradient(160deg,#d9d2c6,#a79884 60%,#5d5348)}
.cta{height:300px;flex:none;display:flex;gap:32px;padding:24px 48px}
.cta-box{width:520px;background:var(--panel);padding:24px 28px}
.cta-box h3{font-size:24px;font-weight:600;color:var(--ink);line-height:1.25}
.cta-box p{color:var(--pink);font-weight:700;font-size:16px;line-height:1.35;margin:8px 0 14px}
.cta-form{display:flex;gap:10px;margin-bottom:10px}
.cta-form .field{width:227px;border:1px solid var(--line)}
.btn-sign{background:var(--green);color:var(--white);font-weight:700;text-align:center;height:40px;line-height:40px;font-size:15px}
.kick{flex:1}
.kick h3{font-family:"Kalam",cursive;color:var(--ink);font-size:32px;margin-bottom:10px}
.kick-card{border:1px solid var(--line);padding:22px;display:flex;gap:20px}
.kick-cover{width:120px;height:150px;flex:none;background:linear-gradient(135deg,var(--pink),#f6a2c0)}
.kick-card h5{color:var(--pink);font-size:16px;font-weight:800;margin-bottom:8px}
.kick-card p{font-size:14px;line-height:1.55;color:var(--muted)}
.site-footer{height:60px;flex:none;display:flex;align-items:center;justify-content:space-between;padding:0 48px;border-top:1px solid var(--line);font-size:12px;color:var(--muted)}
.social{display:flex;align-items:center;gap:8px}
.social b{width:26px;height:26px;display:inline-block;background:var(--pink)}
.band{height:84px;flex:none;background:linear-gradient(180deg,var(--pink-soft),var(--pink))}
</style>
</head>
<body>
<header class="site-header">
  <div class="brand"><span class="brand-dot"></span>Bright Fork Kitchen</div>
  <nav class="main-nav"><span>ABOUT VERITY</span><span>THE MAGAZINE</span><span>BLOG &amp; VIDEOS</span><span class="shop">SHOP</span></nav>
</header>

<section class="hero" role="img" aria-label="Photo of Verity smiling outdoors among green trees">
  <h1>You don't need another diet<br>to get the body you want!</h1>
</section>

<section class="optin-bar">
  <div class="optin-copy">
    <strong>Get my FREE monthly E-Magazine</strong>
    <span>With delicious recipes, inspirational articles, workouts &amp; expert wellness tips that actually work – FREE</span>
  </div>
  <div class="optin-form"><div class="field">First name</div><div class="field">Email</div><div class="btn-yes">YES PLEASE!</div></div>
</section>

<main class="content">
  <article class="article">
    <h2>Want a Body You're Proud Of AND a Healthy Lifestyle You Love?<br>Then You Don't Need Another Diet!</h2>
    <p>Hey there I'm Verity! Fitness coach, author and busy working woman just like you. If you're sick of counting every calorie, skipping dinners out with friends and still not seeing the results you want, I know exactly how you feel. Stick with me, because what you're about to read could change everything.</p>
    <h3>Hmmm... do any of these sound familiar?</h3>
    <ul>
      <li>There's a bunch of clothes that you'd love to wear but they just don't fit</li>
      <li>You feel tired and sluggish by mid afternoon, every single day</li>
      <li>You've tried every diet out there and always end up back at square one</li>
      <li>You feel guilty after every meal and can't enjoy food anymore</li>
      <li>You're constantly stressed, frustrated and short on time</li>
    </ul>
    <p>You're not the only one. I've been there too, and I know how hard it is to keep going when nothing seems to work. The truth is, the problem isn't you. It's the diets you've been told to follow. They're built to be short term, and as soon as they end, old habits come straight back.</p>
    <h3>What If I Told You There Was An Easier &amp; More Enjoyable Way?</h3>
    <ul>
      <li>To lose weight without hunger, cravings or feeling deprived</li>
      <li>Have more energy to enjoy your job, your family and your weekends</li>
      <li>Stop feeling bloated and exhausted after meals</li>
      <li>Stop beating yourself up over every little slip</li>
      <li>Feel great in your clothes, at work and on the weekend</li>
      <li>Feel proud of yourself every time you look in the mirror</li>
      <li>Still have a social life, with wine, dinners and birthday cake</li>
    </ul>
    <p>Ok... sounds good so far, right? But you're probably wondering what is different about this approach. Honestly, the difference is that it's not a diet at all. It's a simple, flexible way of eating real food that fits into your life instead of taking it over. Most plans you've tried before:</p>
    <ul>
      <li>Ignore the importance of pleasure in your life for weight loss</li>
      <li>Don't teach you how to create a routine that lasts for years</li>
      <li>Focus on what you need to cut out rather than what you can add in</li>
      <li>Forget that every woman's body, schedule and goals are different</li>
      <li>Leave you on your own the moment the program finishes</li>
    </ul>
    <p>I get it. I know and understand first hand your frustrations and how much you just want something that finally works.</p>
    <p class="lead">I know you want it to be effective. I know you want to eat tasty food without putting on weight. And you want it to be fun, so it actually sticks.</p>
    <p>You may have tried some of these programs before and felt let down. Maybe you lost a few kilos only to gain them back again. Maybe you felt so restricted that you gave up after a week. I've been there, and that's exactly why I created something better for women like us.</p>
    <p>As a qualified food and fitness coach and personal trainer, I've helped thousands of women learn to eat well, train smart and love the body they live in. My approach is simple: real food, easy workouts and a supportive community that keeps you on track, even on the busiest weeks.</p>
    <p>So what now? Join thousands of readers and subscribe to my free monthly e-magazine for delicious recipes, simple workouts and expert wellness tips delivered straight to your inbox each month.</p>
  </article>

  <aside class="sidebar">
    <div class="endorsed">
      <h4>AS SEEN OR ENDORSED BY</h4>
      <div class="press">Active Her Monthly</div>
      <div class="press">Maison Claudette</div>
      <div class="press">Trim Life Weekly</div>
    </div>
    <div class="promo-photo" role="img" aria-label="Photo of Verity holding her ebook"></div>
  </aside>
</main>

<section class="cta">
  <div class="cta-box">
    <h3>Get Slim, Boost Energy, And Create a Healthy Life You Love!</h3>
    <p>Subscribe to my FREE monthly e-magazine for heaps of awesome recipes, workouts &amp; advice!</p>
    <div class="cta-form"><div class="field">First name</div><div class="field">Email</div></div>
    <div class="btn-sign">SIGN ME UP!</div>
  </div>
  <div class="kick">
    <h3>Need a hand getting started?</h3>
    <div class="kick-card">
      <div class="kick-cover" role="img" aria-label="Cover of the 21 Week Total Momentum Course"></div>
      <div>
        <h5>21 WEEK TOTAL MOMENTUM COURSE</h5>
        <p>An easy-to-follow program to help you get slim and feel well. Use your new habits to create a healthy life you love, one simple week at a time.</p>
      </div>
    </div>
  </div>
</section>

<footer class="site-footer">
  <span>Privacy Policy | Returns &amp; Refunds | Contact</span>
  <div class="social">Connect with Verity <b></b><b></b><b></b><b></b><b></b></div>
</footer>
<div class="band"></div>
</body>
</html>
```